Lumo Brew Premium Matcha brand Label

This is a label design project for a luxury tea brand. Feel free to be creative within the guidelines.
Attached to this project is a document called “Private Label Design Requirements” with the design guidelines and template. There is another document called "Lumo Brew Packaging Instructions" this has more details necessary to stick to the guidelines in the first document.

I have also attached the certifications to be included as well as different variations of the logo for you to use.

If you have any questions, I am here.
Updates

Target Market(s)

Young, active, fun, enjoy the finer things

```html
<!DOCTYPE html>
<html lang="en">
<head>
<meta charset="utf-8">
<title>Lumo Brew Premium Organic Ceremonial Matcha – Jar Label</title>
<link href="https://fonts.googleapis.com/css2?family=Montserrat:wght@500;600;700;800&display=swap" rel="stylesheet">
<style>
  :root {
    --backdrop: #9a9b9f;
    --label-black: #0b0b0c;
    --matcha: #4e8a3c;
    --matcha-light: #8fc27a;
    --matcha-accent: #6fbf4a;
    --paper: #ececec;
    --paper-shade: #c9c9c9;
    --title-grey: #d6d6d6;
    --ink-white: #f2f2f2;
  }
  * { margin: 0; padding: 0; box-sizing: border-box; }
  html, body {
    width: 1200px; height: 430px; overflow: hidden;
    background: var(--backdrop);
    font-family: "Montserrat", sans-serif;
  }
  .label {
    position: absolute; left: 30px; top: 55px;
    width: 1140px; height: 320px;
    border-radius: 6px; overflow: hidden;
    box-shadow: 0 6px 18px rgba(0,0,0,0.25);
  }
  .label-art { position: absolute; inset: 0; width: 100%; height: 100%; }

  .origin-panel {
    position: absolute; left: 60px; top: 118px;
    color: var(--ink-white); font-size: 12.5px; font-weight: 600; line-height: 1.35;
  }
  .origin-panel .certifier { margin-top: 8px; }

  .brand {
    position: absolute; left: 430px; width: 400px; top: 66px;
    display: flex; justify-content: center; align-items: center; gap: 8px;
    color: var(--label-black); font-size: 15px; font-weight: 700;
  }
  .brand-dot { width: 12px; height: 12px; border-radius: 50%; background: var(--label-black); }

  .product-title {
    position: absolute; left: 430px; width: 400px; top: 112px;
    text-align: center; color: var(--title-grey);
    font-size: 27px; font-weight: 800; line-height: 1.08; letter-spacing: 0.3px;
  }
  .net-weight {
    position: absolute; left: 430px; width: 400px; top: 196px;
    text-align: center; color: var(--label-black); font-size: 14px; font-weight: 700;
  }

  .info-panel {
    position: absolute; left: 905px; top: 70px; width: 220px;
    color: var(--ink-white); font-size: 10.5px; font-weight: 600; line-height: 1.35;
  }
  .info-panel h3 { color: var(--matcha-accent); font-size: 15px; font-weight: 700; margin-top: 4px; }
  .info-panel ul { list-style: none; }
  .info-panel li::before { content: "• "; }
  .cert-row { display: flex; align-items: center; gap: 8px; margin-top: 12px; }
  .cert-square { width: 26px; height: 20px; background: #6f8fb3; }
  .cert-circle { width: 22px; height: 22px; border-radius: 50%; background: var(--paper); border: 2px solid var(--matcha); }
  .storage-note { font-size: 10.5px; font-weight: 700; line-height: 1.2; margin-left: 6px; }
</style>
</head>
<body>
  <div class="label">
    <svg class="label-art" viewBox="0 0 1140 320" aria-hidden="false">
      <defs>
        <linearGradient id="paperShade" x1="0" x2="1" y1="0" y2="0">
          <stop offset="0" stop-color="var(--paper)"/>
          <stop offset="1" stop-color="var(--paper-shade)"/>
        </linearGradient>
        <linearGradient id="matchaWash" x1="0" x2="1" y1="0" y2="0">
          <stop offset="0" stop-color="var(--matcha)"/>
          <stop offset="1" stop-color="var(--matcha-light)"/>
        </linearGradient>
      </defs>
      <rect class="label-base" width="1140" height="320" fill="var(--label-black)"/>
      <g role="img" aria-label="Stylised white tea leaf illustration sweeping across the side panel">
        <path d="M215 0 H400 V320 H190 C270 250 300 140 215 0 Z" fill="url(#paperShade)"/>
      </g>
      <path class="front-ground" d="M400 0 H830 V320 H380 C420 220 420 100 400 0 Z" fill="url(#paperShade)"/>
      <path class="front-panel" d="M430 0 H835 V170 C770 290 610 315 530 262 C478 226 448 130 430 0 Z"
            fill="url(#matchaWash)" stroke="var(--label-black)" stroke-width="4"/>
      <path class="side-swoosh" d="M835 0 H920 C885 100 865 165 835 215 Z" fill="var(--matcha)"/>
    </svg>

    <div class="origin-panel">
      <p>Product of Japan<br>Distributed by:<br>Lumo Brew Co. | Fairhaven, Ga</p>
      <p class="certifier">Certified Organic by Verdia</p>
    </div>

    <div class="brand"><span class="brand-dot"></span><span>Lumo Brew</span></div>
    <h1 class="product-title">PREMIUM ORGANIC<br>CEREMONIAL MATCHA</h1>
    <p class="net-weight">Net Wt: 30g</p>

    <div class="info-panel">
      <h3>Ingredients:</h3>
      <p>Premium Organic Japanese Matcha Green Tea</p>
      <h3>Instructions:</h3>
      <ul>
        <li>2 tsp of Matcha</li>
        <li>2oz of Water (170-180 degrees F)</li>
        <li>Whisk in a W formation until frothy</li>
        <li>Sweeten to taste</li>
      </ul>
      <div class="cert-row">
        <span class="cert-square" role="img" aria-label="Non-GMO verification badge"></span>
        <span class="cert-circle" role="img" aria-label="Organic certification badge"></span>
        <span class="storage-note">KEEP REFRIGERATED<br>FOR QUALITY</span>
      </div>
    </div>
  </div>
</body>
</html>
```